Website for Fernvale Harmony Chapel

Wordpress website design required for Fernvale Harmony Chapel. We are a family oriented church catering for age groups from school age to elderly people. The church has a wide variety of activities which it coordinates. The idea is to describe the activities on the activities page, but cross-link them to show which would be applicable to the different age groups.

We would like an inviting website which is easy to read and navigate.

Target Market(s)

Very wide audience - from school age youth to elderly people, so design and style should cater for both audiences.

Industry/Entity Type

Church

Coding

Coded - Design and coding required

Number of Pages Required

5+ page

Font styles to use
Sans Serif

Colors
0255a3
ffffff
0792cd
f78f20

Requirements
Must have
• Inviting website.
• Clear readable font.
• Space to import photos to balance text on each page.
• Need to project a dynamic and progressive feel for the church.
• Easy to navigate.
Nice to have
• Scrolling photos on pages. Ability to enter questions/ comments/prayer requests on Home page.
Should not have
• Conservative audience, so should not be too bold.

```html
<!DOCTYPE html>
<html lang="en">
<head>
<meta charset="utf-8">
<title>Fernvale Harmony Chapel</title>
<link href="https://fonts.googleapis.com/css2?family=Poppins:wght@400;500;700&family=Arimo:wght@400&display=swap" rel="stylesheet">
<style>
  :root {
    --brand-blue: #0255a3;
    --accent-blue: #0077c8;
    --sky-blue: #0792cd;
    --text-grey: #555b61;
    --band-grey: #f1f1f1;
    --strip-grey: #f4f4f4;
    --white: #ffffff;
  }
  * { box-sizing: border-box; margin: 0; padding: 0; }
  html, body { width: 1093px; height: 1200px; overflow: hidden; background: var(--white); }
  body { position: relative; font-family: "Poppins", sans-serif; color: var(--text-grey); }

  .site-header { position: absolute; left: 0; top: 0; width: 1093px; height: 99px; border-bottom: 1px solid #e3e3e3; background: var(--white); }
  .brand { position: absolute; left: 78px; top: 60px; display: flex; align-items: center; gap: 7px; }
  .brand-dot { width: 10px; height: 10px; border-radius: 50%; background: var(--brand-blue); }
  .brand-name { font-weight: 500; font-size: 16px; color: var(--brand-blue); }

  .contact-bar { position: absolute; right: 78px; top: 16px; display: flex; gap: 10px; font-size: 11.5px; color: #7a7f85; align-items: center; }
  .contact-bar span { display: flex; align-items: center; gap: 4px; }
  .contact-bar svg { fill: var(--brand-blue); }

  .main-nav { position: absolute; right: 79px; top: 57px; display: flex; gap: 27px; font-size: 13.5px; color: var(--accent-blue); }
  .main-nav .current { font-weight: 500; color: var(--brand-blue); }

  .hero { position: absolute; left: 0; top: 99px; width: 1093px; height: 373px;
    background:
      radial-gradient(ellipse 22% 45% at 50% 35%, rgba(160,184,198,0.55), rgba(160,184,198,0) 100%),
      radial-gradient(ellipse 16% 40% at 22% 55%, rgba(140,165,180,0.45), rgba(140,165,180,0) 100%),
      radial-gradient(ellipse 16% 40% at 78% 55%, rgba(140,165,180,0.45), rgba(140,165,180,0) 100%),
      radial-gradient(ellipse 60% 80% at 50% 20%, #5e7f94 0%, #3f6178 60%, #2c4c63 100%); }
  .hero-title { position: absolute; left: 0; width: 100%; top: 150px; text-align: center; font-weight: 700; font-size: 25px; color: var(--white); letter-spacing: 0.3px; }
  .hero-text { position: absolute; left: 174px; width: 745px; top: 197px; text-align: center; font-family: "Arimo", sans-serif; font-size: 13.5px; line-height: 19px; color: var(--white); }

  .message-strip { position: absolute; left: 0; top: 472px; width: 1093px; height: 93px; background: var(--strip-grey); }
  .date-box { position: absolute; left: 78px; top: 16px; width: 57px; height: 61px; background: var(--accent-blue); color: var(--white); text-align: center; }
  .date-day { display: block; font-size: 24px; line-height: 24px; margin-top: 10px; }
  .date-month { display: block; font-size: 8px; margin-top: 3px; }
  .service-times { position: absolute; left: 158px; top: 22px; font-size: 12.5px; color: var(--brand-blue); display: flex; gap: 8px; align-items: center; letter-spacing: 0.2px; }
  .service-times svg { stroke: var(--brand-blue); fill: none; }
  .minister-note { position: absolute; left: 158px; top: 47px; font-size: 11.5px; color: var(--text-grey); }
  .read-more { position: absolute; left: 875px; top: 28px; width: 138px; height: 38px; border: 1px solid var(--brand-blue); color: var(--brand-blue); font-size: 15.5px; display: flex; align-items: center; justify-content: center; }

  .section-head { position: absolute; left: 0; width: 1093px; text-align: center; }
  .section-head svg { display: block; margin: 0 auto; stroke: var(--accent-blue); fill: none; }
  .section-title { font-size: 19px; color: var(--accent-blue); font-weight: 400; margin-top: 10px; letter-spacing: 0.4px; }
  .section-sub { font-size: 12.5px; color: var(--text-grey); margin-top: 16px; }

  .activity-grid { position: absolute; left: 78px; top: 693px; width: 934px; height: 359px; }
  .tile { position: absolute; }
  .tile-prayer { left: 0; top: 0; width: 233px; height: 359px;
    background:
      radial-gradient(ellipse 45% 35% at 78% 78%, rgba(246,214,180,0.9), rgba(246,214,180,0) 100%),
      radial-gradient(ellipse 50% 40% at 42% 32%, rgba(238,196,158,0.85), rgba(238,196,158,0) 100%),
      linear-gradient(110deg, #e2c49c 0%, #b8895a 45%, #7a4f2c 80%, #3e2616 100%); }
  .tile-tagline { position: absolute; left: 0; bottom: 0; width: 233px; height: 39px; background: var(--accent-blue); color: var(--white); font-size: 13px; display: flex; align-items: center; padding-left: 40px; }
  .tile-cross { left: 234px; top: 0; width: 233px; height: 179px;
    background:
      radial-gradient(ellipse 40% 30% at 55% 45%, rgba(255,214,120,0.95), rgba(255,214,120,0) 100%),
      linear-gradient(180deg, #6b3e18 0%, #c9802f 35%, #f0b45a 55%, #2a1a0c 78%, #140c06 100%); }
  .tile-pews { left: 234px; top: 180px; width: 233px; height: 179px;
    background:
      radial-gradient(ellipse 35% 30% at 20% 25%, rgba(214,170,140,0.8), rgba(214,170,140,0) 100%),
      linear-gradient(180deg, #b88d72 0%, #7a5240 45%, #4a2e22 75%, #2a1a14 100%); }
  .tile-crucifix { left: 468px; top: 0; width: 233px; height: 359px;
    background:
      radial-gradient(ellipse 30% 45% at 52% 45%, rgba(176,146,108,0.85), rgba(176,146,108,0) 100%),
      radial-gradient(ellipse 70% 80% at 45% 40%, #5e5242, #2e2820 65%, #100d0a 100%); }
  .tile-choir { left: 702px; top: 0; width: 232px; height: 179px;
    background:
      radial-gradient(ellipse 40% 30% at 30% 18%, rgba(240,200,120,0.8), rgba(240,200,120,0) 100%),
      radial-gradient(ellipse 60% 40% at 50% 60%, rgba(196,170,140,0.7), rgba(196,170,140,0) 100%),
      linear-gradient(180deg, #c9ab86 0%, #8d7458 50%, #5a3c28 100%); }
  .tile-glass { left: 702px; top: 180px; width: 232px; height: 179px;
    background:
      radial-gradient(ellipse 30% 35% at 25% 40%, rgba(210,40,40,0.9), rgba(210,40,40,0) 100%),
      radial-gradient(ellipse 30% 35% at 78% 45%, rgba(200,50,60,0.9), rgba(200,50,60,0) 100%),
      radial-gradient(ellipse 25% 30% at 55% 70%, rgba(60,150,70,0.9), rgba(60,150,70,0) 100%),
      radial-gradient(ellipse 30% 25% at 50% 12%, rgba(40,70,170,0.9), rgba(40,70,170,0) 100%),
      linear-gradient(135deg, #1f3c8c, #a82630 45%, #2e7e3c 75%, #c99a24); }

  .news-band { position: absolute; left: 0; top: 1083px; width: 1093px; height: 117px; background: var(--band-grey); }
</style>
</head>
<body>
  <header class="site-header">
    <div class="brand"><span class="brand-dot"></span><span class="brand-name">Fernvale Harmony Chapel</span></div>
    <div class="contact-bar">
      <span><svg width="8" height="10" viewBox="0 0 8 10"><path d="M4 0a4 4 0 0 0-4 4c0 3 4 6 4 6s4-3 4-6a4 4 0 0 0-4-4zm0 5.5A1.5 1.5 0 1 1 4 2.5a1.5 1.5 0 0 1 0 3z"/></svg>14 Larkspur Ave, Fernvale, WA 6090</span>
      <span><svg width="9" height="9" viewBox="0 0 10 10"><path d="M2 0l2 2.5-1 1.2c.6 1.3 1.6 2.3 2.9 2.9l1.2-1L10 8 8.5 10C4 10 0 6 0 1.5z"/></svg>(08) 9400 2718</span>
      <span><svg width="10" height="8" viewBox="0 0 10 8"><path d="M0 0h10v1L5 4 0 1zM0 2l5 3 5-3v6H0z"/></svg>office@fernvaleharmony.org.au</span>
    </div>
    <nav class="main-nav">
      <span class="current">HOME</span><span>Age Group</span><span>Activites</span><span>Events Calendar</span><span>About FHC</span><span>Contact</span>
    </nav>
  </header>

  <section class="hero" role="img" aria-label="Photo of carved stone figures in a church archway, blue-tinted">
    <h1 class="hero-title">Welcome To Fernvale Harmony Chapel</h1>
    <p class="hero-text">welcome text here, welcome text here, welcome text here, welcome text here, welcome text here, welcome text here, wel-come text here, welcome text here, welcome text here, welcome text here, welcome text here, welcome text here, welcome</p>
  </section>

  <section class="message-strip">
    <div class="date-box"><span class="date-day">28</span><span class="date-month">Aug 25</span></div>
    <div class="service-times"><svg width="11" height="11" viewBox="0 0 12 12"><circle cx="6" cy="6" r="5" stroke-width="1.6"/><path d="M6 3v3h2" stroke-width="1.6"/></svg>SATURDAY, @ 8:00 AM | MONDAY, @ 5:00 PM</div>
    <p class="minister-note">"Minister's weekly message, Minister's weekly message, Minister's weekly message, Minister's weekly message, Minister's</p>
    <div class="read-more">Read More</div>
  </section>

  <div class="section-head" style="top:591px;">
    <svg width="22" height="6" viewBox="0 0 22 6"><path d="M1 4q2.5-4 5 0t5 0 5 0 5 0" stroke-width="1.6"/></svg>
    <h2 class="section-title">CHURCH ACTIVITIES</h2>
    <p class="section-sub">Lorem Ipsum is simply dummy text of the printing and typesetting industry.</p>
  </div>

  <section class="activity-grid">
    <div class="tile tile-prayer" role="img" aria-label="Photo of a woman praying with folded hands">
      <div class="tile-tagline">Tagline here, Tagline here</div>
    </div>
    <div class="tile tile-cross" role="img" aria-label="Photo of a cross on a hill at sunset with a kneeling silhouette"></div>
    <div class="tile tile-pews" role="img" aria-label="Photo of a congregation seated in wooden pews"></div>
    <div class="tile tile-crucifix" role="img" aria-label="Photo of a carved crucifix against a dark wall"></div>
    <div class="tile tile-choir" role="img" aria-label="Photo of a congregation singing from hymn books"></div>
    <div class="tile tile-glass" role="img" aria-label="Photo of a colourful stained glass nativity window"></div>
  </section>

  <section class="news-band">
    <div class="section-head" style="top:33px;">
      <svg width="22" height="6" viewBox="0 0 22 6"><path d="M1 4q2.5-4 5 0t5 0 5 0 5 0" stroke-width="1.6"/></svg>
      <h2 class="section-title">NEWS SUMMARIES</h2>
      <p class="section-sub">Lorem Ipsum is simply dummy text of the printing and typesetting industry.</p>
    </div>
  </section>
</body>
</html>
```